Scheduled Servicing Forms

Lumenridge Systems requires two schedule servicing forms to be created on designer templates for our engineers to complete when servicing customers. We will complete these forms on a periodic basis, and send to the customer on completion of the work.
We have two forms that need to be created:
• Hybrid Cloud Customer Service
• Norvex Cloud Customer Service
Please do not reference our website for ideas as its about to change. “Specialised Consulting” is our new go to market, not “Charting the Frontiers of Computing. Our new website (still under development) is available at https://lumenridgesystems.qxv.net.au and will be officially launched shortly.
Our company theme is “Blue” and we want to keep a blue theme for the work.
Please ensure there is “Ample” space for engineers to write comments next to each audit item.
We have uploaded examples of the content that needs to be created for both form in Word and Excel format.
The designer must upload the source files (not just PDF) so we can edit the content on the forms at a later date.
The forms must be in standard A4 size (multiple pages).

```html
<!DOCTYPE html>
<html lang="en">
<head>
<meta charset="utf-8">
<title>Lumenridge Systems – Norvex Cloud Customer Scheduled Service Checklist</title>
<link href="https://fonts.googleapis.com/css2?family=Carlito:wght@400;700&family=Montserrat:wght@500;600&display=swap" rel="stylesheet">
<style>
  :root {
    --navy-deep: #0b1a3f;
    --navy: #123072;
    --blue-bright: #1f55b8;
    --panel: #dde0ea;
    --ink: #111;
    --rule: #333;
    --white: #ffffff;
    --link: #1f4fd1;
  }
  * { box-sizing: border-box; margin: 0; padding: 0; }
  html, body { width: 848px; height: 1200px; overflow: hidden; }
  body { position: relative; font-family: "Carlito", "Calibri", sans-serif; color: var(--ink); }

  .backdrop {
    position: absolute; inset: 0;
    background:
      radial-gradient(ellipse at 20% 15%, #2a5fc4 0%, transparent 45%),
      radial-gradient(ellipse at 90% 90%, #1d4aa8 0%, transparent 40%),
      linear-gradient(160deg, var(--navy) 0%, var(--navy-deep) 60%, #0a1838 100%);
  }

  .brand {
    position: absolute; left: 54px; top: 56px;
    display: flex; align-items: center; gap: 10px;
  }
  .brand-dot { width: 30px; height: 30px; border-radius: 50%; background: var(--white); }
  .brand-name {
    font-family: "Montserrat", sans-serif; font-weight: 600;
    font-size: 17px; letter-spacing: 1px; color: var(--white); text-transform: uppercase;
  }

  .doc-title {
    position: absolute; right: 54px; top: 52px; text-align: right;
    font-family: "Montserrat", sans-serif; color: var(--white); text-transform: uppercase;
  }
  .doc-title .company { font-size: 15px; font-weight: 500; letter-spacing: 0.3px; line-height: 20px; }
  .doc-title .sub { font-size: 11px; font-weight: 500; line-height: 16px; }

  .panel {
    position: absolute; left: 54px; top: 122px; width: 739px; height: 1034px;
    background: var(--panel); border-radius: 21px;
  }

  .checklist {
    position: absolute; left: 19px; top: 16px; width: 702px;
    border: 1px solid var(--rule);
  }
  .item { display: flex; height: 77px; border-top: 1px solid var(--rule); }
  .item:first-child { border-top: none; }
  .task {
    width: 291px; border-right: 1px solid var(--rule);
    padding: 3px 4px 0 7px; font-weight: 700; font-size: 14.6px; line-height: 19px;
  }
  .task a { color: var(--link); }
  .response { flex: 1; padding: 3px 7px 0 7px; font-weight: 700; font-size: 14.6px; line-height: 19px; position: relative; }
  .choices { display: flex; align-items: center; height: 19px; }
  .box { width: 17px; height: 15px; border: 1px solid var(--rule); background: var(--white); }
  .choice-yes { margin-left: 5px; width: 70px; }
  .choice-no { margin-left: 15px; }
  .write-line { position: absolute; left: 7px; right: 7px; top: 55px; border-top: 1px solid var(--rule); }
</style>
</head>
<body>
  <div class="backdrop" role="img" aria-label="Deep blue background with faint circuit-board lines and glowing arcs"></div>

  <div class="brand">
    <span class="brand-dot"></span>
    <span class="brand-name">Lumenridge Systems</span>
  </div>

  <div class="doc-title">
    <div class="company">Lumenridge Systems</div>
    <div class="sub">Norvex Cloud Customer</div>
    <div class="sub">Scheduled Service Checklist</div>
  </div>

  <main class="panel">
    <div class="checklist">
      <div class="item"><div class="task">Review Network Firewall Firmware is up to date andno ANY &lt;&gt;ANY rulesin place</div><div class="response"><div class="choices"><span class="box"></span><span class="choice-yes">YES</span><span class="box"></span><span class="choice-no">NO</span></div>Comment:<span class="write-line"></span></div></div>
      <div class="item"><div class="task">Ensure critical network equipment is connected to UPS (min 20min run time)</div><div class="response"><div class="choices"><span class="box"></span><span class="choice-yes">YES</span><span class="box"></span><span class="choice-no">NO</span></div>Comment:<span class="write-line"></span></div></div>
      <div class="item"><div class="task">Ensure Access Layer Network device firmware is up to date (Switches &amp;Access Points)</div><div class="response"><div class="choices"><span class="box"></span><span class="choice-yes">YES</span><span class="box"></span><span class="choice-no">NO</span></div>Comment:<span class="write-line"></span></div></div>
      <div class="item"><div class="task">Ensure the latest backup configuration for managed network devices is current or automatically backed up monthly. Saved Network location must be secured</div><div class="response"><div class="choices"><span class="box"></span><span class="choice-yes">YES</span><span class="box"></span><span class="choice-no">NO</span></div>Comment:<span class="write-line" style="top:53px"></span></div></div>
      <div class="item"><div class="task">Ensure MFP’s &amp;Printersdrivers up to date. No Print Nightmare</div><div class="response"><div class="choices"><span class="box"></span><span class="choice-yes">YES</span><span class="box"></span><span class="choice-no">NO</span></div>Comment:<span class="write-line"></span></div></div>
      <div class="item"><div class="task">NAC Certificates are current (PEAP/EAP-TLS)</div><div class="response"><div class="choices"><span class="box"></span><span class="choice-yes">YES</span><span class="box"></span><span class="choice-no">NO</span></div>Comment:<span class="write-line"></span></div></div>
      <div class="item"><div class="task">Check DLP alerts and configuration</div><div class="response"><div class="choices"><span class="box"></span><span class="choice-yes">YES</span><span class="box"></span><span class="choice-no">NO</span></div>Comment:<span class="write-line"></span></div></div>
      <div class="item"><div class="task">Review &amp; address SIEM and SOC alerts</div><div class="response"><div class="choices"><span class="box"></span><span class="choice-yes">YES</span><span class="box"></span><span class="choice-no">NO</span></div>Comment:<span class="write-line"></span></div></div>
      <div class="item"><div class="task">Email alerting on firewall changessent to <a href="mailto:alerts@lmrg.net.au">alerts@lmrg.net.au</a></div><div class="response"><div class="choices"><span class="box"></span><span class="choice-yes">YES</span><span class="box"></span><span class="choice-no">NO</span></div>Comment:<span class="write-line"></span></div></div>
      <div class="item"><div class="task">Review Vulnerability Scan reports; Remediate as required</div><div class="response"><div class="choices"><span class="box"></span><span class="choice-yes">YES</span><span class="box"></span><span class="choice-no">NO</span></div>Comment:<span class="write-line"></span></div></div>
      <div class="item"><div class="task">Confirm all Infrastructure is in Monitoring</div><div class="response"><div class="choices"><span class="box"></span><span class="choice-yes">YES</span><span class="box"></span><span class="choice-no">NO</span></div>Comment:<span class="write-line"></span></div></div>
      <div class="item"><div class="task">Check vendor Maintenance period of all infrastructure</div><div class="response"><div class="choices"><span class="box"></span><span class="choice-yes">YES</span><span class="box"></span><span class="choice-no">NO</span></div>Comment:<span class="write-line"></span></div></div>
      <div class="item"><div class="task">Check time sync across all/critical devices</div><div class="response"><div class="choices"><span class="box"></span><span class="choice-yes">YES</span><span class="box"></span><span class="choice-no">NO</span></div>Comment:<span class="write-line"></span></div></div>
    </div>
  </main>
</body>
</html>
```